MODERN + COOL Business Card Needed!

SUMMARY
This is for a 40+ year old family business that is transitioning to the 2nd generation and is in real need of a more modern facelift. Ive attached a company logo (I made quickly as an idea with my limited PSD skills) to start off with that you are welcome to change and draw ideas from. Ive also attached some screen shots of cards I like to give you an idea of my preferences.

WHAT WE DO
The company name is Tall Pine HK Ltd. But I prefer to just call it Tall Pine or Tall Pine with Hong Kong as kind of a sub heading on the business card. We own a factory as well as help our customers find factories to make their product. Product I mean, toys 99.9% of the time. Simple old school toys like board games, puzzles, wooden toys, baby/infant toys.

You can say we are a "sourcing" or "trading" or "consulting" company with a factory to help you do it. But since we deal with toys, i like to keep it modern and cool and fun, not serious like managing hedge funds.

WHAT WE ARE LOOKING FOR
A cool, unique looking business card that stands out. In terms of design, something modern and professional. I like darker colored cards and I like colors such as blue/green/dark gray, but am open to other colored themes. I Like bright lime green with gray, always though thats a nice combo. I prefer cards that are all colored and not so much white showing (I think). Ive attached a few screenshots of cards so take a look to get a feel of what I like.

We do alot of wooden stacking games in variety of colors too like Tovra, Lumo, Towerplix (google these to check them out). So designs that sort of resemble stacking or building would be cool but totally not necessary.

In terms of the physical aspects of the card, Im looking for a card a bit different than the standard rectangular shape. Double sided. Little things like having corner(s) be round or different angle instead of square edge I always thought was nice. Its got to be mostly a normal card size, no folding or smaller cards that fit weird in your wallet. No vertical designs. Am open to VERY different/creative shapes (as long as it still fits in a wallet good like a normal buisness card.
Updates

Hi everyone!

Just wanted to write a message to everyone to let them know all submissions are being reviewed or have been reviewed.  If I have not responded with feedback, rest assure your submission was definitely looked at in detail but I either have just been too busy to respond (alot of submissions!), or its on my to be considered list.

I respect and really enjoy receiving everyones creativity and work so I dont want it to go unrecognized - thus this message!  Feel free to submit more ideas if you like until this project ends.  Sometimes some designs just dont click but sometimes they can so you never know!

Thanks again for everyones participation and great work!

~Dev Orr

Target Market(s)

The cards are mainly handed to toy company sourcers and buyers. People I talk to ... say Pelvane for example... might want to make their next edition of Farthingale game with a reputable factory at a good cost so they can sell it to stores at a profit.

So these are the types of people I often try to talk and introduce myself and my company to.

Industry/Entity Type

Building

Colors
acd036
0392cd
00a88e
474747
606060

Requirements
Must have
• Just double sided, not plain rectangle corners, and just cool to look at and catches your eye!

Oh and the obvious business card stuff like place for name, address, number, email, etc.
Nice to have
• Think more modern and fun, not serious and old fashion (thats what we used to be!). Can use the logo I attached and you can definitely alter and change the logo or make a whole new one!

Oh and can definitely use a creative slogan if you like to think of one based on what I described in what we do.
Should not have
• Dont use fonts or text placement that might make "Tall Pine" look like "Tal Lpine"... We arent selling news papers!!

Please nothing related to education since we have the word Pine in the title, thats not our business at all.

Logo and design should not be too heavy on things related to toys, as though thats what we primarily focus on now, what we do may change over time.

```html
<!DOCTYPE html>
<html lang="en">
<head>
<meta charset="utf-8">
<title>Tall Pine Ltd — Business Card, Front and Back</title>
<link rel="stylesheet" href="https://fonts.googleapis.com/css2?family=Tinos:wght@400;700&family=Open+Sans:wght@400&display=swap">
<style>
  :root {
    --page: #ffffff;
    --card: #474747;
    --lime: #acd036;
    --ink-light: #ffffff;
    --ink-dark: #111111;
    --frame: #222222;
  }
  html, body {
    margin: 0;
    padding: 0;
    width: 1200px;
    height: 1200px;
    overflow: hidden;
    background: var(--page);
  }
  .sheet {
    display: block;
    width: 1200px;
    height: 1200px;
  }
  .sheet-frame { fill: none; stroke: var(--frame); stroke-width: 1.5; }
  .side-label {
    font-family: "Open Sans", Arial, sans-serif;
    font-size: 29px;
    fill: var(--ink-dark);
  }
  .card-shape { fill: var(--card); }
  .brand-disc { fill: var(--lime); stroke: var(--ink-light); stroke-width: 3; }
  .brand-name-mark {
    font-family: "Tinos", "Times New Roman", serif;
    font-weight: 700;
    font-size: 62px;
    fill: var(--ink-light);
  }
  .company-name {
    font-family: "Tinos", "Times New Roman", serif;
    font-weight: 700;
    font-size: 56px;
    letter-spacing: -1px;
    fill: var(--ink-light);
  }
  .company-place {
    font-family: "Tinos", "Times New Roman", serif;
    font-weight: 700;
    font-size: 33px;
    fill: var(--ink-light);
  }
  .person-name {
    font-family: "Tinos", "Times New Roman", serif;
    font-size: 25px;
    fill: var(--ink-light);
  }
  .person-role, .contact-line {
    font-family: "Tinos", "Times New Roman", serif;
    font-size: 12.5px;
    fill: var(--ink-light);
  }
</style>
</head>
<body>
<svg class="sheet" viewBox="0 0 1209 1209" xmlns="http://www.w3.org/2000/svg" aria-label="Tall Pine Ltd business card, front and back">
  <rect class="sheet-frame" x="0.75" y="0.75" width="1207.5" height="1207.5"/>

  <!-- Front side -->
  <g class="card card-front">
    <text class="side-label" x="59" y="299">Front</text>
    <path class="card-shape" d="M437,63 H1006 V536 H437 A236.5 236.5 0 0 1 437,63 Z"/>
    <circle class="brand-disc" cx="417" cy="300" r="197"/>
    <text class="brand-name-mark" x="417" y="320" text-anchor="middle">Tall Pine</text>
    <text class="company-name" x="812" y="301" text-anchor="middle">tall pine ltd</text>
    <text class="company-place" x="812" y="333" text-anchor="middle">hong kong</text>
  </g>

  <!-- Back side -->
  <g class="card card-back">
    <text class="side-label" x="59" y="928">Back</text>
    <path class="card-shape" d="M203,673 H770 A236 236 0 0 1 770,1145 H203 Z"/>
    <circle class="brand-disc" cx="792" cy="910" r="197"/>
    <text class="brand-name-mark" x="792" y="930" text-anchor="middle">Tall Pine</text>
    <text class="person-name" x="388" y="911" text-anchor="middle">Dev Orr</text>
    <text class="person-role" x="388" y="927" text-anchor="middle">Managing Director</text>
    <text class="contact-line" x="388" y="1087" text-anchor="middle">Email: devorr@tallpineltd.com</text>
    <text class="contact-line" x="388" y="1108" text-anchor="middle">www.tallpineltd.com</text>
  </g>
</svg>
</body>
</html>
```